Real Estate Agent Service Brochure

I need a trifold brochure to showcase my real estate services. I am a veteran Real Estate Broker specializing in marketing properties for sale and for top dollar. I would like to see designs that use colors from my logo (attached) and I would like to showcase some before and after photos of staging jobs I have done to homes to get them ready for the market. This brochure is specific to home sellers. You are happy to go check out my website for inspiration www.lomavertpa.com but keep the copy as I have written it. The the final design should communicate experienced professional who uses current technologies and strategies to market properties for the highest value.

Target Market(s)

Homeowners wanting to sell their homes

Industry/Entity Type

Real Estate Agent

Font styles to use
Serif

Requirements
Must have
• My, logo, personal photo, title and contact information as listed:
• Marta Venholt
• Owner Broker
• Stager Re-Designer
• 860-912-7048
• BRAVE Realty LLC
• LOMAVERTPA.com
• Marta@LOMAVERTPA.com
• The colors used should be those in my logo.
• Brochure should be able to fit in standard envelope for mailing.
Nice to have
• I think I would like my personal photo and contact information on the front panel.
Should not have
• Bright colors.

```html
<!DOCTYPE html>
<html lang="en">
<head>
<meta charset="utf-8">
<title>Marta Venholt – Seller Brochure, Inside Spread</title>
<link href="https://fonts.googleapis.com/css2?family=Open+Sans:wght@400;600;700;800&display=swap" rel="stylesheet">
<style>
  :root {
    --navy: #16205a;
    --navy-deep: #101849;
    --ink: #1d1d24;
    --paper: #ffffff;
    --stage: #d9d9db;
    --band: #3a3a40;
    --mist: #ececee;
    --label-light: #ffffff;
  }
  * { box-sizing: border-box; margin: 0; padding: 0; }
  html, body { width: 1200px; height: 800px; overflow: hidden; }
  body {
    background: var(--stage);
    font-family: "Open Sans", Arial, sans-serif;
    color: var(--ink);
  }
  .brochure {
    position: absolute; left: 36px; top: 35px;
    width: 1128px; height: 730px;
    display: flex;
    background: var(--paper);
    box-shadow: 0 6px 22px rgba(0,0,0,.18);
  }
  .panel {
    position: relative; width: 376px; height: 100%;
    overflow: hidden;
    background: linear-gradient(180deg, var(--paper) 0%, var(--paper) 45%, var(--mist) 100%);
  }
  .panel + .panel { border-left: 1px solid #e2e2e4; }

  .staging-photo { position: absolute; left: 0; width: 100%; }
  .staging-photo svg { display: block; width: 100%; height: 100%; }
  .staging-label {
    position: absolute; font-weight: 800; font-size: 22px; letter-spacing: .5px;
    text-transform: uppercase; line-height: 1;
  }
  .staging-label--after { color: var(--navy); text-shadow: 0 0 3px rgba(255,255,255,.8); }
  .staging-label--before { color: var(--label-light); text-shadow: 0 1px 3px rgba(0,0,0,.6); }

  .copy {
    position: absolute; left: 38px; right: 38px;
    font-size: 14px; line-height: 1.32; text-align: justify;
  }
  .copy p + p { margin-top: 12px; }

  .intro-block {
    position: absolute; left: 0; top: 0; width: 100%; height: 340px;
    background: var(--navy);
    color: var(--paper);
    padding: 34px 34px 0;
    font-size: 14px; line-height: 1.34; text-align: justify;
  }
</style>
</head>
<body>
<main class="brochure">

  <!-- Panel: selling today -->
  <section class="panel panel--left">
    <div class="staging-photo" style="top:0;height:320px;">
      <svg viewBox="0 0 376 320" preserveAspectRatio="none">
        <defs>
          <linearGradient id="livingBefore" x1="0" y1="0" x2="1" y2="1">
            <stop offset="0" stop-color="#8a6a4a"/><stop offset="1" stop-color="#4a3826"/>
          </linearGradient>
          <linearGradient id="livingAfter" x1="0" y1="0" x2="1" y2="1">
            <stop offset="0" stop-color="#d8cfc2"/><stop offset="1" stop-color="#9c8a76"/>
          </linearGradient>
        </defs>
        <g role="img" aria-label="Before photo: living room with stone fireplace, unstaged">
          <polygon points="0,0 376,0 376,200 0,80" fill="url(#livingBefore)"/>
        </g>
        <g role="img" aria-label="After photo: same living room staged with furniture and decor">
          <polygon points="0,92 376,212 376,320 0,320" fill="url(#livingAfter)"/>
        </g>
        <polygon points="0,80 376,200 376,212 0,92" fill="var(--band)"/>
        <path d="M0,250 Q188,200 376,290 L376,320 L0,320 Z" fill="var(--band)"/>
        <path d="M0,262 Q188,212 376,302 L376,320 L0,320 Z" fill="var(--paper)"/>
      </svg>
      <span class="staging-label staging-label--after" style="left:22px;top:112px;">After</span>
      <span class="staging-label staging-label--before" style="right:22px;top:160px;">Before</span>
    </div>
    <div class="copy" style="top:360px;">
      <p>Selling Real Estate has changed drastically in the last few years. Today’s real estate processes are multi faceted undertakings that encompass significant emotional and financial components. Having the right marketing partner is so important; one who works to protect your best interests while capably navigating you through the many complexities of the real estate transaction is vital.</p>
      <p>Marta Venholt Residential Marketing Real Estate Specialist truly understands not only the legal process needed but also recognizes buyer trends and knows how to “showcase” a property to sell targeted to the proper consumer demographic.</p>
    </div>
  </section>

  <!-- Panel: why hire -->
  <section class="panel panel--center">
    <div class="staging-photo" style="top:300px;height:430px;">
      <svg viewBox="0 0 376 430" preserveAspectRatio="none">
        <defs>
          <linearGradient id="bedBefore" x1="0" y1="0" x2="1" y2="1">
            <stop offset="0" stop-color="#cfc6b8"/><stop offset="1" stop-color="#5a4a3c"/>
          </linearGradient>
          <linearGradient id="bedAfter" x1="0" y1="0" x2="1" y2="1">
            <stop offset="0" stop-color="#b7b2aa"/><stop offset="1" stop-color="#ecebe8"/>
          </linearGradient>
        </defs>
        <g role="img" aria-label="Before photo: empty bedroom with dark wood floor">
          <polygon points="0,0 376,0 376,260 0,150" fill="url(#bedBefore)"/>
        </g>
        <g role="img" aria-label="After photo: same bedroom staged with bed, nightstand and chandelier">
          <polygon points="0,162 376,272 376,430 0,430" fill="url(#bedAfter)"/>
        </g>
        <polygon points="0,150 376,260 376,272 0,162" fill="var(--band)"/>
      </svg>
      <span class="staging-label staging-label--after" style="left:24px;top:184px;">After</span>
      <span class="staging-label staging-label--before" style="right:22px;top:210px;">Before</span>
    </div>
    <svg style="position:absolute;left:0;top:300px;width:376px;height:60px;" viewBox="0 0 376 60" preserveAspectRatio="none">
      <path d="M0,0 L376,0 L376,50 Q188,10 0,40 Z" fill="var(--band)"/>
      <path d="M0,0 L376,0 L376,38 Q188,0 0,28 Z" fill="var(--navy)"/>
    </svg>
    <div class="intro-block">
      A home is one of your most valuable assets. If you are thinking about selling a property, it is crucial that you hire someone with an extraordinary history of happy sellers. Marta devotes her efforts to selling real estate, by keeping up with the evolving market, researching buyer trends and preparing homes before they enter the market by staging them to connect with the target buyer. Marta knows all sales are not alike. Therefore, taking a cookie cutter approach is not acceptable, she recognizes that each property is unique and requires a personalized marketing strategy.
    </div>
  </section>

  <!-- Panel: experience -->
  <section class="panel panel--right">
    <div class="staging-photo" style="top:0;height:340px;">
      <svg viewBox="0 0 376 340" preserveAspectRatio="none">
        <defs>
          <linearGradient id="kitBefore" x1="0" y1="0" x2="1" y2="1">
            <stop offset="0" stop-color="#c9b9a0"/><stop offset="1" stop-color="#3e2e22"/>
          </linearGradient>
          <linearGradient id="kitAfter" x1="0" y1="0" x2="1" y2="1">
            <stop offset="0" stop-color="#e4ddd0"/><stop offset="1" stop-color="#6e5a44"/>
          </linearGradient>
        </defs>
        <g role="img" aria-label="Before photo: kitchen with cluttered dining table">
          <polygon points="0,0 376,0 376,110 0,110" fill="url(#kitBefore)"/>
        </g>
        <g role="img" aria-label="After photo: same kitchen staged with island and set dining table">
          <polygon points="0,122 376,122 376,340 0,340" fill="url(#kitAfter)"/>
        </g>
        <polygon points="0,110 376,110 376,122 0,122" fill="var(--band)"/>
        <path d="M0,270 Q188,230 376,290 L376,340 L0,340 Z" fill="var(--band)"/>
        <path d="M0,282 Q188,242 376,302 L376,340 L0,340 Z" fill="var(--paper)"/>
      </svg>
      <span class="staging-label staging-label--after" style="left:22px;top:132px;">After</span>
      <span class="staging-label staging-label--before" style="right:22px;top:82px;">Before</span>
    </div>
    <div class="copy" style="top:430px;">
      <p>A veteran in the real estate industry with nearly 30 years of real estate expertise and consistent membership in the Multi-Million-Dollar Club combined with her ACS Home Stager and Re-Designer credentials assures that her clients get the advantage of vast knowledge, seasoned experience and proven results, all geared to creating beautiful spaces, which form a connection with the right buyer producing the highest and best offer.</p>
    </div>
  </section>

</main>
</body>
</html>
```